Keystone Prime Water Tank

I primarily market the water tanks so want a business care that reflects that. I have attached the water tank logo. You have been working on our water tank so maybe we can use that on the card et. I am leaving as one sided but can be double sided if that works. The information that needs to be on the cards is as follows: Gerald T. Munro Phone numbers: Office 555-284-9137 Direct 555-619-2405 Mobile 555-372-5841 email address: gerald@fieldgearworks.com Address P.O. Box 8273 Millbrook, GA 30512 Web Page: www.fieldgearworks.com. A lot to fit on the card. Thanks

```html
<!DOCTYPE html>
<html lang="en">
<head>
<meta charset="utf-8">
<title>Keystone Prime Water Tank – Business Card</title>
<link rel="stylesheet" href="https://fonts.googleapis.com/css2?family=Open+Sans:wght@400;700;800&display=swap">
<style>
  :root {
    --backdrop: #3b3b3b;
    --card-white: #ffffff;
    --card-black: #121212;
    --brand-red: #e31e24;
    --ink: #1c1c1c;
    --ink-soft: #4a4a4a;
    --emboss: #3a3a3a;
  }
  * { box-sizing: border-box; margin: 0; padding: 0; }
  html, body { width: 1200px; height: 801px; overflow: hidden; }
  body {
    background: var(--backdrop);
    font-family: "Open Sans", Arial, sans-serif;
    display: flex;
    align-items: center;
    justify-content: center;
    gap: 60px;
  }
  .card {
    width: 500px;
    height: 286px;
    position: relative;
    border-bottom: 3px solid var(--brand-red);
    border-left: 2px solid var(--brand-red);
  }
  .card-front {
    background: var(--card-white);
    display: flex;
    align-items: center;
    padding: 0 28px 0 30px;
  }
  .brand-name {
    width: 190px;
    color: var(--ink);
    font-weight: 800;
    font-size: 25px;
    line-height: 1.1;
    text-transform: uppercase;
    display: flex;
    align-items: center;
    gap: 10px;
  }
  .brand-mark {
    flex: none;
    width: 16px;
    height: 16px;
    background: var(--brand-red);
  }
  .divider {
    width: 2px;
    height: 170px;
    background: var(--brand-red);
    margin: 0 20px 0 14px;
  }
  .contact { color: var(--ink-soft); font-size: 12.5px; line-height: 1.5; }
  .contact-name {
    color: var(--brand-red);
    font-weight: 700;
    font-size: 19px;
    margin-bottom: 4px;
  }
  .address { margin-bottom: 6px; }
  .contact-line { display: flex; align-items: center; gap: 7px; white-space: nowrap; }
  .contact-line svg { width: 11px; height: 11px; flex: none; }
  .label { color: var(--brand-red); font-size: 11px; }
  .card-back {
    background: var(--card-black);
    display: flex;
    align-items: center;
    justify-content: center;
  }
  .back-brand {
    color: var(--emboss);
    font-weight: 800;
    font-size: 34px;
    line-height: 1.1;
    text-transform: uppercase;
    text-align: center;
    display: flex;
    align-items: center;
    gap: 14px;
  }
  .back-brand .brand-mark { background: var(--emboss); width: 22px; height: 22px; }
</style>
</head>
<body>
  <section class="card card-front">
    <div class="brand-name"><span class="brand-mark"></span>Keystone Prime Water Tank</div>
    <div class="divider"></div>
    <div class="contact">
      <p class="contact-name">Gerald T. Munro</p>
      <p class="address">P.O. Box 8273<br>Millbrook, GA 30512</p>
      <p class="contact-line">
        <svg viewBox="0 0 12 12"><path fill="#e31e24" d="M2.5 1l2 2-1 1.3a6 6 0 0 0 3.2 3.2l1.3-1 2 2-1.5 1.5C5.5 10 2 6.5 1 2.5z"/></svg>
        555-284-9137 <span class="label">Office</span>
      </p>
      <p class="contact-line">
        <svg viewBox="0 0 12 12"><path fill="#e31e24" d="M2.5 1l2 2-1 1.3a6 6 0 0 0 3.2 3.2l1.3-1 2 2-1.5 1.5C5.5 10 2 6.5 1 2.5z"/></svg>
        555-619-2405 <span class="label">Direct</span>
      </p>
      <p class="contact-line">
        <svg viewBox="0 0 12 12"><rect x="3" y="1" width="6" height="10" rx="1" fill="none" stroke="#e31e24" stroke-width="1.3"/></svg>
        555-372-5841 <span class="label">Mobile</span>
      </p>
      <p class="contact-line">
        <svg viewBox="0 0 12 12"><rect x="1" y="2.5" width="10" height="7" fill="#e31e24"/><path d="M1 2.5l5 4 5-4" fill="none" stroke="#fff" stroke-width="1"/></svg>
        gerald@fieldgearworks.com
      </p>
      <p class="contact-line">
        <svg viewBox="0 0 12 12"><circle cx="6" cy="6" r="5" fill="#e31e24"/><path d="M1 6h10M6 1c-2.5 3-2.5 7 0 10M6 1c2.5 3 2.5 7 0 10" fill="none" stroke="#fff" stroke-width=".8"/></svg>
        www.fieldgearworks.com
      </p>
    </div>
  </section>

  <section class="card card-back">
    <div class="back-brand"><span class="brand-mark"></span>Keystone Prime<br>Water Tank</div>
  </section>
</body>
</html>
```